Marketing Flyer for Plumber Referals

8.5" x11" Layout should be landscape not portrait. Create a bold, eye-catching flyer that highlights earning potential from referrals for water damage restoration. Use high-contrast colors like blue, yellow, and white, with bold fonts and dynamic layouts. Include images of restoration work, cash, and happy clients. Emphasize key benefits like $500 minimum payouts, fast payments, and unlimited income potential. Keep instructions simple: refer a client, we handle the work, you get paid. Add a clear call-to-action and display contact details prominently. Focus on professionalism and energy.

Target Market(s)

Plumbers and Contractor 8.5" x11" Layout should be landscape not portrait.

Industry/Entity Type

General Contractor

Colors
0054AA
0677BA
7BADD7
CADEEF
E8F1F8
EB3D1F
EC4F4E
F09395
F8D3D4
FCEDEE

Requirements
Must have
• 8.5" x11" Layout should be landscape not portrait.
Nice to have

```html
<!DOCTYPE html>
<html lang="en">
<head>
<meta charset="utf-8">
<title>Get Paid to Refer a Flood</title>
<link rel="stylesheet" href="https://fonts.googleapis.com/css2?family=Montserrat:ital,wght@0,400;0,500;0,600;1,400;1,600;1,800;1,900&display=swap">
<style>
  :root {
    --brand-blue: #0a3f96;
    --brand-blue-deep: #073786;
    --brand-yellow: #f7d40f;
    --white: #ffffff;
    --cash-tone-a: #3d64b0;
    --cash-tone-b: #0a3f96;
    --water-tone-a: #d8d4cc;
    --water-tone-b: #5a5650;
    --portrait-tone-a: #e6e8ea;
    --portrait-tone-b: #6f7f92;
  }
  * { margin: 0; padding: 0; box-sizing: border-box; }
  html, body { width: 1200px; height: 927px; overflow: hidden; background: var(--white); }
  body { font-family: "Montserrat", sans-serif; color: var(--brand-blue); }

  .flyer { position: relative; width: 1200px; height: 927px; overflow: hidden; background: var(--white); }

  .hero-band { position: absolute; left: 0; top: 0; width: 1200px; height: 415px; background: var(--brand-blue); }

  .cash-photo {
    position: absolute; left: 0; top: 0; width: 430px; height: 242px;
    background: linear-gradient(120deg, var(--cash-tone-a) 0%, var(--cash-tone-b) 100%);
    opacity: .85;
  }

  .brand-panel {
    position: absolute; left: 908px; top: 0; width: 230px; height: 185px;
    background: var(--brand-blue-deep); border-radius: 0 0 22px 22px;
    display: flex; align-items: center; justify-content: center;
  }
  .brand-name {
    font-family: "Montserrat", sans-serif; font-weight: 500; font-size: 15px;
    letter-spacing: 1.5px; color: var(--white); text-transform: uppercase; margin-top: 40px;
  }

  .headline { position: absolute; left: 60px; top: 52px; font-style: italic; font-weight: 900; line-height: 78px; font-size: 64px; letter-spacing: -2px; }
  .headline-top { color: var(--brand-yellow); display: block; }
  .headline-bottom { color: var(--white); display: block; }

  .restoration-photo {
    position: absolute; left: 0; top: 242px; width: 880px; height: 275px;
    background: linear-gradient(180deg, var(--water-tone-a) 0%, #b9b0a2 45%, var(--water-tone-b) 100%);
  }

  .process-strip { position: absolute; left: 0; top: 440px; }

  .section-title {
    position: absolute; left: 62px; top: 462px; font-size: 41px; font-weight: 900; font-style: italic;
    letter-spacing: -1.5px; color: var(--brand-blue);
  }

  .client-portrait-ring {
    position: absolute; left: 807px; top: 216px; width: 330px; height: 330px; border-radius: 50%;
    background: var(--brand-yellow);
  }
  .client-portrait {
    position: absolute; left: 824px; top: 233px; width: 296px; height: 296px; border-radius: 50%;
    background: radial-gradient(circle at 50% 40%, var(--portrait-tone-a) 0%, #b7bec6 55%, var(--portrait-tone-b) 100%);
  }

  .step { position: absolute; top: 575px; width: 250px; }
  .step-1 { left: 60px; } .step-2 { left: 309px; } .step-3 { left: 568px; }
  .step-icon { position: relative; width: 103px; height: 103px; }
  .step-number {
    position: absolute; left: 65px; top: -6px; width: 36px; height: 36px; border-radius: 50%;
    background: var(--brand-yellow); color: var(--brand-blue); font-weight: 800; font-style: italic;
    font-size: 17px; display: flex; align-items: center; justify-content: center;
  }
  .step-title { margin-top: 28px; font-size: 20.5px; font-weight: 800; font-style: italic; line-height: 26px; height: 62px; }
  .step-text { margin-top: 10px; font-size: 21px; font-weight: 500; line-height: 26px; }

  .contact-card { position: absolute; left: 818px; top: 571px; }
  .contact-heading {
    position: absolute; left: 853px; top: 596px; font-size: 26px; font-weight: 900; font-style: italic;
    line-height: 31px; letter-spacing: -.5px; color: var(--brand-blue);
  }
  .contact-item { position: absolute; font-size: 22px; font-style: italic; font-weight: 600; line-height: 26px; color: var(--brand-blue); }
  .contact-phone { left: 913px; top: 703px; }
  .contact-web { left: 936px; top: 774px; }

  .footer-tab { position: absolute; top: 906px; width: 101px; height: 30px; border-radius: 16px 16px 0 0; background: var(--brand-yellow); }
  .footer-tab-1 { left: 60px; } .footer-tab-2 { left: 314px; } .footer-tab-3 { left: 573px; }
</style>
</head>
<body>
<main class="flyer">
  <div class="hero-band"></div>
  <div class="cash-photo" role="img" aria-label="Fanned stack of hundred dollar bills"></div>

  <div class="brand-panel"><span class="brand-name">Harborview Remodel</span></div>

  <h1 class="headline"><span class="headline-top">GET PAID TO</span><span class="headline-bottom">REFER A FLOOD</span></h1>

  <div class="restoration-photo" role="img" aria-label="Flooded home interior with water covering the floor at the foot of a staircase"></div>

  <svg class="process-strip" width="900" height="95" viewBox="0 0 900 95" aria-hidden="true">
    <path d="M0 77 H870 Q880 77 880 87 L880 94 H0 Z" fill="var(--brand-yellow)"/>
    <path d="M0 2 H383 Q400 2 404 18 L416 77 H0 Z" fill="var(--brand-yellow)"/>
  </svg>
  <h2 class="section-title">How It Works</h2>

  <div class="client-portrait-ring"></div>
  <div class="client-portrait" role="img" aria-label="Portrait of a smiling happy client"></div>

  <section class="step step-1">
    <div class="step-icon">
      <svg width="103" height="103" viewBox="0 0 103 103" aria-hidden="true">
        <circle cx="51.5" cy="51.5" r="51.5" fill="var(--brand-yellow)"/>
        <circle cx="51.5" cy="51.5" r="44" fill="var(--brand-blue)"/>
        <g fill="none" stroke="var(--white)" stroke-width="2.5" stroke-linecap="round">
          <path d="M36 44 q0-10 10-9 q4-7 12-2 q10-1 9 8 q4 6-4 8 H40 q-6-1-4-5z"/>
          <rect x="27" y="60" width="50" height="10" rx="4"/>
          <path d="M52 49 v11"/>
        </g>
      </svg>
      <span class="step-number">1</span>
    </div>
    <h3 class="step-title">Refer Flood, Water<br>and Mold Damage</h3>
    <p class="step-text">Call, book online,<br>or text us directly.</p>
  </section>

  <section class="step step-2">
    <div class="step-icon">
      <svg width="103" height="103" viewBox="0 0 103 103" aria-hidden="true">
        <circle cx="51.5" cy="51.5" r="51.5" fill="var(--brand-yellow)"/>
        <circle cx="51.5" cy="51.5" r="44" fill="var(--brand-blue)"/>
        <g fill="none" stroke="var(--white)" stroke-width="2.5" stroke-linejoin="round" stroke-linecap="round">
          <path d="M51.5 46 l-9-9 a6 6 0 0 1 9-8 a6 6 0 0 1 9 8z"/>
          <path d="M28 44 l2 18 l12 12 v4 M75 44 l-2 18 l-12 12 v4"/>
        </g>
      </svg>
      <span class="step-number">2</span>
    </div>
    <h3 class="step-title">We Take Care<br>of Everything</h3>
    <p class="step-text">Free evaluations,<br>insurance claims, and<br>professional service.</p>
  </section>

  <section class="step step-3">
    <div class="step-icon">
      <svg width="103" height="103" viewBox="0 0 103 103" aria-hidden="true">
        <circle cx="51.5" cy="51.5" r="51.5" fill="var(--brand-yellow)"/>
        <circle cx="51.5" cy="51.5" r="44" fill="var(--brand-blue)"/>
        <g fill="none" stroke="var(--white)" stroke-width="2.5" stroke-linecap="round">
          <rect x="28" y="46" width="26" height="18" rx="2"/>
          <path d="M41 50 v10 M44 52 h-5 a2 2 0 0 0 0 4 h4 a2 2 0 0 1 0 4 h-5"/>
          <rect x="60" y="32" width="14" height="28" rx="2"/>
        </g>
      </svg>
      <span class="step-number">3</span>
    </div>
    <h3 class="step-title">Get Paid Fast</h3>
    <p class="step-text">$500 minimum or 10%<br>of the invoice within 48<br>hours of final payment.</p>
  </section>

  <svg class="contact-card" width="382" height="296" viewBox="0 0 382 296" aria-hidden="true">
    <path d="M60 0 H382 V294 H110 Q70 294 55 250 L4 60 Q-6 0 60 0 Z" fill="var(--brand-yellow)"/>
    <line x1="39" y1="110" x2="322" y2="110" stroke="var(--brand-blue)" stroke-width="3"/>
    <line x1="105" y1="182" x2="322" y2="182" stroke="#c9a94a" stroke-width="1"/>
    <circle cx="60" cy="144" r="5" fill="none" stroke="var(--brand-blue)" stroke-width="3"/>
    <circle cx="86" cy="230" r="5" fill="none" stroke="var(--brand-blue)" stroke-width="3"/>
    <g fill="none" stroke="var(--brand-blue)" stroke-width="2.5" stroke-linecap="round" stroke-linejoin="round">
      <path d="M272 30 q-8 4-6 14 q6 18 24 30 q9 5 14-3 l-8-8 q-4 4-8 1 q-8-6-12-14 q-2-4 2-7 z"/>
      <path d="M290 30 a14 14 0 0 1 12 12 M292 22 a22 22 0 0 1 18 18"/>
    </g>
  </svg>
  <p class="contact-heading">Call Text or<br>Book On-line</p>
  <p class="contact-item contact-phone">555-214-0398</p>
  <p class="contact-item contact-web">HarborviewBuilds<br>.com</p>

  <div class="footer-tab footer-tab-1"></div>
  <div class="footer-tab footer-tab-2"></div>
  <div class="footer-tab footer-tab-3"></div>
</main>
</body>
</html>
```